Namecard Designs+Logo for a High End Automobile Company

We need a new business card for our company called Velta Motorhof.

www.veltamotorhof.example.sg
Our new website will be up in 2.5 months time.

We sell used and brand new continental cars like Korvane, QTL, Dravell, Solbrini and etc. Currently we are operating from 2 offices in Singapore and United Kingdom.

We want a design which is serious. We are open to colours but try to keep it at a maximum of 3 colours.

We prefer something simple and minimal. We are open to 2 sides printing or even 2 sided namecards. Both UK and Singapore company offices address must be in; either side by side, front and back, or even 2 sided cards.

The logo can be a text logo, emblem, abstract, pictorial or combination.

We are printing with Pribo.com so please kindly follow the printing guideline.

http://uk.pribo.example/help/faq/templates-and-guidelines.html

Rich and Car Enthusiasts

Printing

Must have
• Our 2 offices; UK and Singapore.

Our slogan which is " The Automobile Specialist"
Should not have
• Not more than 3 colours

```html
<!DOCTYPE html>
<html lang="en">
<head>
<meta charset="utf-8">
<title>Velta Motorhof – Business Card</title>
<link href="https://fonts.googleapis.com/css2?family=Arimo:ital,wght@0,400;0,700;1,400&family=Ubuntu:wght@300;500&display=swap" rel="stylesheet">
<style>
  :root {
    --ink: #111111;
    --paper: #ffffff;
    --olive: #a6a838;
    --olive-dark: #6f7024;
    --card-black: #050505;
    --backdrop: #3b1c14;
  }
  * { margin: 0; padding: 0; box-sizing: border-box; }
  html, body { width: 1200px; height: 808px; overflow: hidden; }
  body { position: relative; background: var(--backdrop); font-family: "Arimo", Arial, sans-serif; }

  .brand-strip { position: absolute; left: 0; top: 0; width: 1200px; height: 196px; background: var(--paper); }
  .wordmark { font-family: "Arimo", Arial, sans-serif; font-weight: 700; color: var(--ink); letter-spacing: -0.5px; white-space: nowrap; }
  .brand-strip .wordmark { position: absolute; left: 68px; top: 52px; font-size: 58px; line-height: 1; }

  .card { position: absolute; width: 545px; height: 302px; border-radius: 22px; }
  .card-front { left: 70px; top: 390px; background: var(--paper); }
  .card-back { left: 598px; top: 376px; background: var(--card-black); color: var(--paper); }

  .slogan { position: absolute; right: 50px; top: 105px; font-size: 17px; font-weight: 700; color: var(--olive); letter-spacing: 0.4px; white-space: nowrap; }
  .card-front .wordmark { position: absolute; right: 50px; top: 132px; font-size: 48px; line-height: 1; }

  .holder { position: absolute; right: 58px; top: 36px; text-align: right; }
  .holder-name { font-family: "Ubuntu", sans-serif; font-size: 26px; font-weight: 300; line-height: 1; }
  .holder-name strong { font-weight: 500; }
  .holder-role { margin-top: 8px; margin-right: 10px; font-size: 13px; font-style: italic; color: var(--olive); letter-spacing: 0.3px; }

  .rule-set { position: absolute; left: 20px; top: 94px; }

  .office { position: absolute; top: 150px; font-size: 16px; line-height: 21px; }
  .office-sg { left: 56px; color: var(--paper); }
  .office-uk { left: 295px; color: var(--olive); }
  .office h2 { font-size: 19px; font-weight: 700; margin-bottom: 24px; line-height: 22px; }
</style>
</head>
<body>
  <header class="brand-strip">
    <div class="wordmark">Velta Motorhof</div>
  </header>

  <section class="card card-front">
    <p class="slogan">THE AUTOMOBILE SPECIALIST</p>
    <div class="wordmark">Velta Motorhof</div>
  </section>

  <section class="card card-back">
    <div class="holder">
      <p class="holder-name">Aldous <strong>Brenner</strong></p>
      <p class="holder-role">COMPANY DIRECTOR</p>
    </div>

    <svg class="rule-set" width="525" height="22" viewBox="0 0 525 22" aria-hidden="true">
      <rect x="0" y="0" width="525" height="2" fill="var(--olive)"/>
      <rect x="0" y="7" width="525" height="4" fill="var(--olive)"/>
      <rect x="0" y="15" width="525" height="5" fill="var(--olive-dark)"/>
    </svg>

    <div class="office office-sg">
      <h2>singapore</h2>
      <p>t. 020 414 262 62</p>
      <p>f. 020 393 717 71</p>
      <p>e. ab@veltamotorhof.example</p>
    </div>

    <div class="office office-uk">
      <h2>united kingdom</h2>
      <p>t. 020 414 262 62</p>
      <p>f. 020 393 717 71</p>
      <p>e. ab@veltamotorhof.example</p>
    </div>
  </section>
</body>
</html>
```